New Townhome community needs for sale sign.

need a 4 foot by 8 foot banner to put on building listing newly constructed townhomes as "coming soon" to market. Construction is scheduled to be completed Dec 2024. Sale of units will begin Spring of 2025.
6 individual townhome units each 2,000 square feet. each unit is 3 bedroom 2.5 bathroom with 2 car garage and each has a rooftop "sky lounge" with amazing views. Gated community. Units available for sale Spring of 2025. Real estate company selling units will be KTL & Associates. Will need KTL & Associates Logo on the banner. Would like to keep with the same blue color scheme as the KTL & Associates logo. phone number on banner to be 480-555-3164. web ktlpartners.example.

```html
<!DOCTYPE html>
<html lang="en">
<head>
<meta charset="utf-8">
<title>KTL &amp; Associates – Townhomes Coming Soon Banner</title>
<link rel="stylesheet" href="https://fonts.googleapis.com/css2?family=Montserrat:wght@800&family=Catamaran:wght@600;700&family=Roboto+Condensed:wght@700&display=swap">
<style>
  :root {
    --frame: #3a3a3c;
    --deep-blue: #1e6f9c;
    --sky-blue: #23a6d8;
    --white: #ffffff;
    --charcoal: #333335;
  }
  html, body {
    margin: 0;
    padding: 0;
    width: 1200px;
    height: 600px;
    overflow: hidden;
    background: var(--frame);
  }
  .banner { display: block; width: 1200px; height: 600px; }
  .frame { fill: var(--frame); }
  .panel-main { fill: var(--deep-blue); }
  .panel-features { fill: var(--sky-blue); }
  .divider { fill: var(--white); }
  .wave-band { fill: var(--sky-blue); }
  .wave-base { fill: var(--white); }

  .headline {
    font-family: "Montserrat", sans-serif;
    font-weight: 800;
    font-size: 76px;
    fill: var(--white);
  }
  .intro {
    font-family: "Catamaran", sans-serif;
    font-weight: 600;
    font-size: 34px;
    fill: var(--white);
  }
  .sales-box { fill: var(--white); }
  .sales-text {
    font-family: "Catamaran", sans-serif;
    font-weight: 700;
    font-size: 34px;
    fill: var(--deep-blue);
  }
  .units-box { fill: var(--white); }
  .units-text {
    font-family: "Catamaran", sans-serif;
    font-weight: 700;
    font-size: 28px;
    fill: var(--deep-blue);
  }
  .feature {
    font-family: "Catamaran", sans-serif;
    font-weight: 600;
    font-size: 29px;
    fill: var(--white);
  }
  .bullet-ring { fill: none; stroke: var(--white); stroke-width: 2; }
  .bullet-dot { fill: var(--white); }
  .rule { stroke: var(--white); stroke-width: 2; }
  .availability-label {
    font-family: "Catamaran", sans-serif;
    font-weight: 600;
    font-size: 17px;
    fill: var(--white);
  }
  .availability-date {
    font-family: "Catamaran", sans-serif;
    font-weight: 700;
    font-size: 36px;
    fill: var(--white);
  }
  .brand-mark { fill: var(--deep-blue); }
  .brand-name {
    font-family: "Catamaran", sans-serif;
    font-weight: 700;
    font-size: 50px;
    fill: var(--charcoal);
  }
  .contact-label-band { fill: var(--sky-blue); }
  .contact-details-band { fill: var(--deep-blue); }
  .contact-text {
    font-family: "Roboto Condensed", sans-serif;
    font-weight: 700;
    fill: var(--white);
  }
  .contact-label { font-size: 30px; }
  .contact-item { font-size: 27px; }
</style>
</head>
<body>
<svg class="banner" viewBox="0 0 1200 600" xmlns="http://www.w3.org/2000/svg" role="img" aria-label="Coming soon banner for newly constructed townhomes by KTL &amp; Associates">
  <rect class="frame" x="0" y="0" width="1200" height="600"/>

  <!-- Panels -->
  <rect class="panel-main" x="38" y="28" width="1124" height="503"/>
  <polygon class="panel-features" points="710,28 1162,28 1162,531 625,531"/>
  <polygon class="divider" points="695,28 710,28 647,402 633,402"/>

  <!-- Waves -->
  <path class="wave-band" d="M38,466 C150,392 300,362 420,366 C600,372 900,452 1162,470 L1162,531 L38,531 Z"/>
  <path class="wave-base" d="M38,486 C160,408 310,380 420,382 C620,388 900,472 1162,490 L1162,531 L38,531 Z"/>

  <!-- Headline block -->
  <text class="headline" x="90" y="146">COMING SOON</text>
  <text class="intro" x="91" y="196">Newly Constructed Townhomes</text>
  <text class="intro" x="91" y="232">Construction Completion:</text>
  <text class="intro" x="91" y="268">December 2024</text>

  <rect class="sales-box" x="90" y="288" width="439" height="46"/>
  <text class="sales-text" x="102" y="325">SALES BEGIN: SPRING 2025</text>

  <!-- Features -->
  <rect class="units-box" x="728" y="77" width="280" height="60" rx="6"/>
  <text class="units-text" x="747" y="106">6 INDIVIDUAL</text>
  <text class="units-text" x="747" y="130">TOWNHOME UNITS</text>

  <g class="feature-list">
    <g class="bullet"><circle class="bullet-ring" cx="719" cy="163" r="9"/><circle class="bullet-dot" cx="719" cy="163" r="5"/></g>
    <text class="feature" x="748" y="171">2,000 sq. ft. each</text>

    <g class="bullet"><circle class="bullet-ring" cx="719" cy="199" r="9"/><circle class="bullet-dot" cx="719" cy="199" r="5"/></g>
    <text class="feature" x="748" y="207">3 Bedrooms, 2.5 Bathrooms</text>

    <g class="bullet"><circle class="bullet-ring" cx="719" cy="236" r="9"/><circle class="bullet-dot" cx="719" cy="236" r="5"/></g>
    <text class="feature" x="748" y="244">2 Car Garage</text>

    <g class="bullet"><circle class="bullet-ring" cx="719" cy="272" r="9"/><circle class="bullet-dot" cx="719" cy="272" r="5"/></g>
    <text class="feature" x="748" y="280">Rooftop "Sky Lounge"</text>
    <text class="feature" x="763" y="316">with Amazing Views</text>

    <g class="bullet"><circle class="bullet-ring" cx="719" cy="344" r="9"/><circle class="bullet-dot" cx="719" cy="344" r="5"/></g>
    <text class="feature" x="748" y="352">Gated Community</text>
  </g>

  <line class="rule" x1="680" y1="371" x2="1122" y2="371"/>

  <text class="availability-label" x="950" y="402" text-anchor="middle">Units Available for Sale</text>
  <text class="availability-date" x="962" y="435" text-anchor="middle">SPRING OF 2025</text>

  <!-- Brand -->
  <rect class="brand-mark" x="231" y="472" width="46" height="46"/>
  <text class="brand-name" x="290" y="518">KTL &amp; Associates</text>

  <!-- Contact ribbon -->
  <polygon class="contact-label-band" points="66,531 345,531 345,576 50,576"/>
  <polygon class="contact-details-band" points="345,531 1134,531 1149,576 345,576"/>
  <text class="contact-text contact-label" x="76" y="565">Contact Information:</text>
  <text class="contact-text contact-item" x="355" y="564">KTL &amp; Associates</text>
  <text class="contact-text contact-item" x="562" y="564">Phone: 480-555-3164</text>
  <text class="contact-text contact-item" x="818" y="564" textLength="305" lengthAdjust="spacingAndGlyphs">Website: ktlpartners.example</text>
</svg>
</body>
</html>
```